Locksmith Services Tri Fold Flyer

We are a security company that provide all forms of security, we are looking to have tri fold flyers created for each service we offer starting with Locksmith Services, I am looking to work with someone who can design the layout and advise where the text would go where the pictures would go etc as well as tweaking our current logo, I am hoping to find someone that I can work with across all marketing materials for the business.

Our company is called Harborline Venture Collective , and the Locksmith side will be Harborline Locksmiths which is why the logo will need tweaking but with the text " Part of the Harborline Venture Collective "

Our Strap Line is " Protecting People, Property & Assets "

```html
<!DOCTYPE html>
<html lang="en">
<head>
<meta charset="utf-8">
<title>Harborline Locksmiths – Tri Fold Flyer</title>
<link href="https://fonts.googleapis.com/css2?family=Montserrat:wght@400;500;600;700;800&family=Cinzel:wght@500&display=swap" rel="stylesheet">
<style>
  :root{
    --gold:#c9a96b;
    --gold-deep:#b08f50;
    --ink:#111111;
    --black:#050505;
    --paper:#ffffff;
    --canvas:#ededed;
    --text:#2a2a2a;
    --muted:#d6d6d6;
  }
  *{box-sizing:border-box;margin:0;padding:0}
  html,body{width:1200px;height:2400px;overflow:hidden}
  body{background:var(--canvas);font-family:"Montserrat",Arial,sans-serif;color:var(--text);position:relative}
  .spread{position:absolute;left:30px;width:1140px;height:880px;background:var(--paper);box-shadow:0 6px 24px rgba(0,0,0,.18);overflow:hidden}
  .spread--outside{top:220px}
  .spread--inside{top:1200px}
  .panel{position:absolute;top:0;height:880px;width:380px}
  .gold{color:var(--gold)}
  .icon-sym{display:none}

  /* Panel: about */
  .about{left:0;background:var(--paper)}
  .photo{position:absolute}
  .about__photo{left:0;top:0;width:380px;height:270px;background:linear-gradient(180deg,#6f6f6f 0%,#a9a9a9 45%,#e9e9e9 85%,#fff 100%)}
  .about__body{position:absolute;left:34px;top:250px;width:320px}
  .h-section{font-weight:800;font-size:20px;color:var(--ink);letter-spacing:-.3px;margin-bottom:16px}
  .about p{font-size:12.6px;line-height:1.25;text-align:justify;margin-bottom:18px;color:#333}
  .team{font-weight:800;font-size:17.5px;line-height:1.3;color:var(--ink);letter-spacing:-.3px;margin-top:6px}
  .team span{display:block;color:var(--gold)}
  .ticks{list-style:none;margin-top:16px}
  .ticks li{position:relative;padding-left:26px;font-size:12.6px;line-height:1.25;margin-bottom:13px;color:#333}
  .ticks li svg{position:absolute;left:0;top:1px;width:15px;height:15px}
  .web{position:absolute;bottom:38px;left:0;width:100%;text-align:center;font-weight:600;font-size:16.5px;color:var(--ink)}
  .web--light{color:#fff}

  /* Panel: contact */
  .contact{left:380px;background:linear-gradient(90deg,#000 0%,#111 100%);color:#fff;text-align:center}
  .brand{position:absolute;left:0;width:380px;top:60px;display:flex;justify-content:center;align-items:center;gap:10px}
  .brand__dot{width:44px;height:44px;border-radius:50%;background:var(--gold)}
  .brand__name{font-weight:700;font-size:16px;color:var(--gold);line-height:1.2;text-align:left}
  .strap{position:absolute;left:0;width:380px;top:152px;font-family:"Cinzel",Georgia,serif;font-size:10.5px;color:var(--gold);text-align:center;letter-spacing:.3px}
  .contact__list{position:absolute;top:192px;left:0;width:380px;list-style:none}
  .contact__list li{height:80px;display:flex;flex-direction:column;align-items:center}
  .contact__icon{width:38px;height:38px;border-radius:50%;background:var(--gold);border:2px solid #3a3a3a;box-shadow:0 0 0 1px var(--gold);display:flex;align-items:center;justify-content:center;margin-bottom:8px}
  .contact__icon svg{width:18px;height:18px}
  .contact__list span{font-size:16px;font-weight:500}
  .emergency{position:absolute;display:flex;align-items:center;gap:12px}
  .contact .emergency{top:510px;left:60px}
  .badge247{width:58px;height:58px;border-radius:50%;border:3px solid #fff;outline:2px dashed #777;outline-offset:2px;display:flex;align-items:center;justify-content:center;font-weight:700;font-size:15px;color:#fff}
  .emergency__text{text-align:left;line-height:.95}
  .emergency__text b{display:block;color:var(--gold);font-weight:700;font-size:26px;letter-spacing:-.3px}
  .emergency__text strong{display:block;color:#fff;font-weight:800;font-size:31px;letter-spacing:1px}
  .tollfree{position:absolute;height:32px;width:320px;border-radius:16px;border:1.5px solid #ddd;display:flex;overflow:hidden;font-weight:700;font-size:16px;letter-spacing:.5px}
  .tollfree__label{background:var(--gold);color:var(--ink);width:172px;display:flex;align-items:center;justify-content:center;border-radius:16px 0 0 16px;clip-path:polygon(0 0,100% 0,88% 100%,0 100%)}
  .tollfree__num{flex:1;display:flex;align-items:center;justify-content:center;color:#fff;margin-left:-14px}
  .contact .tollfree{top:600px;left:30px}
  .contact__photo{left:0;top:640px;width:380px;height:240px;background:radial-gradient(ellipse at 60% 55%,#8a8a8a 0%,#3a3a3a 45%,#0a0a0a 80%)}

  /* Panel: cover */
  .cover{left:760px;background:var(--paper)}
  .cover__art{position:absolute;left:0;top:0;width:380px;height:670px}
  .cover .brand{top:60px}
  .cover .strap{top:152px}
  .cover__title{position:absolute;top:685px;left:0;width:380px;text-align:center;color:var(--ink);font-weight:800;line-height:1}
  .cover__title .l1{font-size:28px;letter-spacing:-.5px}
  .cover__title .l2{font-size:47px;color:var(--gold);letter-spacing:-1px;margin:2px 0}
  .cover__title .l3{font-size:30px;letter-spacing:-.5px}
  .rule{position:absolute;left:40px;width:300px;top:810px;height:1px;background:#aaa}

  /* Inside: services */
  .services{position:absolute;left:0;top:0;width:760px;height:880px;background:var(--black);color:#fff}
  .services__title{position:absolute;left:34px;top:36px;font-weight:800;font-size:22px;letter-spacing:-.4px;color:#fff}
  .services__line{position:absolute;left:326px;top:60px;width:408px;height:1px;background:#888}
  .services__underline{position:absolute;left:34px;top:72px;width:30px;height:2px;background:var(--gold)}
  .svc-grid{position:absolute;left:34px;top:100px;width:700px;display:grid;grid-template-columns:1fr 1fr;column-gap:48px;row-gap:22px}
  .svc{display:flex;gap:12px;height:62px}
  .svc__icon{flex:0 0 58px;width:58px;height:58px;border-radius:50%;background:var(--gold);border:3px solid var(--black);box-shadow:0 0 0 1.5px #cfcfcf;display:flex;align-items:center;justify-content:center}
  .svc__icon svg{width:28px;height:28px}
  .svc h3{font-size:13px;font-weight:700;margin-top:2px;margin-bottom:4px}
  .svc p{font-size:12px;line-height:1.2;color:#e4e4e4}
  .services__photo{left:330px;top:600px;width:430px;height:280px;background:radial-gradient(ellipse at 55% 45%,#8c8c8c 0%,#444 40%,#050505 78%)}
  .services .emergency{top:690px;left:40px}
  .services .tollfree{top:788px;left:36px}
  .services .web--light{left:370px;bottom:40px;width:auto;text-align:left}

  /* Inside: help */
  .help{left:760px;background:var(--paper)}
  .help__art{position:absolute;left:0;top:0;width:380px;height:270px}
  .help__body{position:absolute;left:22px;top:284px;width:338px}
  .help h2{font-weight:800;font-size:17px;color:var(--ink);letter-spacing:-.4px;margin-bottom:16px}
  .help h4{font-size:12px;font-weight:700;color:var(--ink);line-height:1.25;margin-bottom:10px}
  .help p{font-size:12px;line-height:1.25;text-align:justify;color:#333;margin-bottom:14px}
  .help h5{font-size:13px;font-weight:600;color:var(--gold);margin-bottom:8px}
  .price{text-align:center;color:var(--ink);font-weight:800;margin-top:10px}
  .price .p1{font-size:17px;letter-spacing:-.3px}
  .price .p2{font-size:34px;letter-spacing:-.8px;line-height:1.1}
</style>
</head>
<body>

<svg class="icon-sym" aria-hidden="true">
  <symbol id="i-tick" viewBox="0 0 16 16"><circle cx="8" cy="8" r="8" fill="#c9a96b"/><path d="M4.5 8.2l2.3 2.3 4.7-4.8" fill="none" stroke="#fff" stroke-width="1.8"/></symbol>
  <symbol id="i-phone" viewBox="0 0 24 24"><path d="M6.6 10.8a15 15 0 006.6 6.6l2.2-2.2a1 1 0 011-.25 11.4 11.4 0 003.6.57 1 1 0 011 1V20a1 1 0 01-1 1A17 17 0 013 4a1 1 0 011-1h3.5a1 1 0 011 1c0 1.25.2 2.45.57 3.6a1 1 0 01-.25 1z" fill="#111"/></symbol>
  <symbol id="i-mail" viewBox="0 0 24 24"><rect x="3" y="5" width="18" height="14" rx="1.5" fill="none" stroke="#111" stroke-width="2"/><path d="M3.5 6l8.5 7 8.5-7" fill="none" stroke="#111" stroke-width="2"/></symbol>
  <symbol id="i-pin" viewBox="0 0 24 24"><path d="M12 2a7 7 0 00-7 7c0 5 7 13 7 13s7-8 7-13a7 7 0 00-7-7z" fill="#111"/><circle cx="12" cy="9" r="2.6" fill="#c9a96b"/></symbol>
  <symbol id="i-globe" viewBox="0 0 24 24"><circle cx="12" cy="12" r="9" fill="none" stroke="#111" stroke-width="2"/><path d="M3 12h18M12 3c3 3 3 15 0 18M12 3c-3 3-3 15 0 18" fill="none" stroke="#111" stroke-width="1.6"/></symbol>
  <symbol id="i-clock" viewBox="0 0 24 24"><circle cx="12" cy="12" r="9" fill="none" stroke="#111" stroke-width="1.8"/><path d="M12 7v5l3 2" fill="none" stroke="#111" stroke-width="1.8"/></symbol>
  <symbol id="i-door" viewBox="0 0 24 24"><rect x="9" y="3" width="11" height="18" fill="none" stroke="#111" stroke-width="1.8"/><path d="M3 12h9M9 9l3 3-3 3" fill="none" stroke="#111" stroke-width="1.8"/></symbol>
  <symbol id="i-lock" viewBox="0 0 24 24"><rect x="5" y="10" width="14" height="11" rx="1.5" fill="none" stroke="#111" stroke-width="1.8"/><path d="M8 10V7a4 4 0 018 0v3" fill="none" stroke="#111" stroke-width="1.8"/><circle cx="12" cy="15" r="1.6" fill="#111"/></symbol>
  <symbol id="i-key" viewBox="0 0 24 24"><circle cx="8" cy="12" r="4" fill="none" stroke="#111" stroke-width="1.8"/><path d="M12 12h9M18 12v3M21 12v3" fill="none" stroke="#111" stroke-width="1.8"/></symbol>
  <symbol id="i-people" viewBox="0 0 24 24"><circle cx="8" cy="9" r="2.5" fill="none" stroke="#111" stroke-width="1.6"/><circle cx="16" cy="9" r="2.5" fill="none" stroke="#111" stroke-width="1.6"/><path d="M3.5 19a4.5 4.5 0 019 0M11.5 19a4.5 4.5 0 019 0" fill="none" stroke="#111" stroke-width="1.6"/></symbol>
  <symbol id="i-shield" viewBox="0 0 24 24"><path d="M12 3l8 3v6c0 5-4 8-8 9-4-1-8-4-8-9V6z" fill="none" stroke="#111" stroke-width="1.8"/><path d="M8.5 12l2.5 2.5 4.5-5" fill="none" stroke="#111" stroke-width="1.8"/></symbol>
  <symbol id="i-house" viewBox="0 0 24 24"><path d="M3 11l9-7 9 7M5 10v10h14V10" fill="none" stroke="#111" stroke-width="1.8"/><rect x="10" y="14" width="4" height="6" fill="none" stroke="#111" stroke-width="1.6"/></symbol>
  <symbol id="i-grid" viewBox="0 0 24 24"><rect x="4" y="4" width="16" height="16" rx="1" fill="none" stroke="#111" stroke-width="1.8"/><path d="M4 12h16M12 4v16" fill="none" stroke="#111" stroke-width="1.6"/></symbol>
  <symbol id="i-question" viewBox="0 0 24 24"><circle cx="12" cy="12" r="9" fill="none" stroke="#111" stroke-width="1.8"/><path d="M9.5 9.5a2.5 2.5 0 015 0c0 1.8-2.5 2-2.5 4" fill="none" stroke="#111" stroke-width="1.8"/><circle cx="12" cy="17" r="1.1" fill="#111"/></symbol>
</svg>

<!-- Outside spread -->
<section class="spread spread--outside">

  <article class="panel about">
    <div class="photo about__photo" role="img" aria-label="Black and white photo of a locksmith using a cordless drill on a door handle"></div>
    <div class="about__body">
      <h2 class="h-section">ABOUT <span class="gold">US</span></h2>
      <p>Lorem Ipsum is simply dummy text of the printing and typesetting industry. Lorem Ipsum has been the industry's standard dummy text ever since the 1500s, when an unknown printer took a galley of type and scrambled it to make a type specimen book. It has survived not only five centuries, but also the leap into electronic typesetting, remaining essentially unchanged. It was popularised in the 1960s with the release of Typeset sheets containing Lorem Ipsum passages, and more recently with desktop publishing software like LayoutPro including versions of Lorem Ipsum.</p>
      <p>Contrary to popular belief, Lorem Ipsum is not simply random text. It has roots in a piece of classical Latin literature from 45 BC, making it over 2000 years old.</p>
      <h3 class="team">OUR TEAM OF LOCKSMITHS<span>USE THE LATEST MACHINERY</span><span>ON THE MARKET</span></h3>
      <ul class="ticks">
        <li><svg><use href="#i-tick"/></svg>Allows us to cut keys much faster at our shop</li>
        <li><svg><use href="#i-tick"/></svg>Get an exact cut of your original key</li>
        <li><svg><use href="#i-tick"/></svg>Allow us to cut both house keys as well as car keys</li>
      </ul>
    </div>
    <div class="web">www.harborlinelocks.com</div>
  </article>

  <article class="panel contact">
    <div class="brand"><span class="brand__dot"></span><span class="brand__name">Harborline<br>Locksmiths</span></div>
    <div class="strap">PROTECTING PEOPLE, PROPERTY &amp; ASSETS</div>
    <ul class="contact__list">
      <li><span class="contact__icon"><svg><use href="#i-phone"/></svg></span><span>014.782.3360</span></li>
      <li><span class="contact__icon"><svg><use href="#i-mail"/></svg></span><span>hello@harborlinelocks.com</span></li>
      <li><span class="contact__icon"><svg><use href="#i-pin"/></svg></span><span>Your company address</span></li>
      <li><span class="contact__icon"><svg><use href="#i-globe"/></svg></span><span>www.harborlinelocks.com</span></li>
    </ul>
    <div class="emergency">
      <div class="badge247">24/7</div>
      <div class="emergency__text"><b>EMERGENCY</b><strong>SERVICES</strong></div>
    </div>
    <div class="tollfree"><span class="tollfree__label">TOLL FREE NO</span><span class="tollfree__num">0800-417-2293</span></div>
    <div class="photo contact__photo" role="img" aria-label="Black and white photo of a hand turning a key in a door lock"></div>
  </article>

  <article class="panel cover">
    <svg class="cover__art" viewBox="0 0 380 670" role="img" aria-label="Photo of a locksmith kneeling to drill a lock on a front door, framed in a shield shape">
      <defs>
        <linearGradient id="coverPhoto" x1="0" y1="0" x2="0" y2="1">
          <stop offset="0" stop-color="#000"/>
          <stop offset=".22" stop-color="#0d0d0d"/>
          <stop offset=".45" stop-color="#5f5a52"/>
          <stop offset=".75" stop-color="#8a8070"/>
          <stop offset="1" stop-color="#a89a82"/>
        </linearGradient>
      </defs>
      <path d="M0 0H380V510C380 575 250 565 190 655C130 565 0 575 0 510Z" fill="var(--gold)"/>
      <path d="M0 0H380V480C372 550 248 548 190 630C132 548 8 550 0 480Z" fill="url(#coverPhoto)"/>
    </svg>
    <div class="brand"><span class="brand__dot"></span><span class="brand__name">Harborline<br>Locksmiths</span></div>
    <div class="strap">PROTECTING PEOPLE, PROPERTY &amp; ASSETS</div>
    <h1 class="cover__title"><div class="l1">PROTECTING PEOPLE</div><div class="l2">PROPERTY</div><div class="l3">AND ASSETS</div></h1>
    <div class="rule"></div>
    <div class="web">www.harborlinelocks.com</div>
  </article>
</section>

<!-- Inside spread -->
<section class="spread spread--inside">
  <div class="services">
    <div class="photo services__photo" role="img" aria-label="Black and white photo of a hand holding a car key"></div>
    <h2 class="services__title">OUR <span class="gold">LOCKSMITH SERVICES</span> ||||</h2>
    <div class="services__line"></div>
    <div class="services__underline"></div>
    <div class="svc-grid">
      <div class="svc"><span class="svc__icon"><svg><use href="#i-clock"/></svg></span><div><h3>Emergency Call Outs</h3><p>Lorem Ipsum is simply dummy text of the printing and typesetting industry. Lorem Ipsum has been the industry's.</p></div></div>
      <div class="svc"><span class="svc__icon"><svg><use href="#i-lock"/></svg></span><div><h3>Locks</h3><p>Lorem Ipsum is simply dummy text of the printing and typesetting industry. Lorem Ipsum has been the industry's.</p></div></div>
      <div class="svc"><span class="svc__icon"><svg><use href="#i-door"/></svg></span><div><h3>Gain Entry</h3><p>Lorem Ipsum is simply dummy text of the printing and typesetting industry. Lorem Ipsum has been the industry's.</p></div></div>
      <div class="svc"><span class="svc__icon"><svg><use href="#i-people"/></svg></span><div><h3>Physical Security</h3><p>Lorem Ipsum is simply dummy text of the printing and typesetting industry. Lorem Ipsum has been the industry's.</p></div></div>
      <div class="svc"><span class="svc__icon"><svg><use href="#i-key"/></svg></span><div><h3>Business Locksmiths</h3><p>Lorem Ipsum is simply dummy text of the printing and typesetting industry. Lorem Ipsum has been the industry's.</p></div></div>
      <div class="svc"><span class="svc__icon"><svg><use href="#i-house"/></svg></span><div><h3>Architectural Ironmongery</h3><p>Lorem Ipsum is simply dummy text of the printing and typesetting industry. Lorem Ipsum has been the industry's.</p></div></div>
      <div class="svc"><span class="svc__icon"><svg><use href="#i-house"/></svg></span><div><h3>Domestic Locksmiths</h3><p>Lorem Ipsum is simply dummy text of the printing and typesetting industry. Lorem Ipsum has been the industry's.</p></div></div>
      <div class="svc"><span class="svc__icon"><svg><use href="#i-key"/></svg></span><div><h3>Master Keyed Systems</h3><p>Lorem Ipsum is simply dummy text of the printing and typesetting industry. Lorem Ipsum has been the industry's.</p></div></div>
      <div class="svc"><span class="svc__icon"><svg><use href="#i-grid"/></svg></span><div><h3>Key Cutting</h3><p>Lorem Ipsum is simply dummy text of the printing and typesetting industry. Lorem Ipsum has been the industry's.</p></div></div>
      <div class="svc"><span class="svc__icon"><svg><use href="#i-door"/></svg></span><div><h3>Smart Access Control</h3><p>Lorem Ipsum is simply dummy text of the printing and typesetting industry. Lorem Ipsum has been the industry's.</p></div></div>
      <div class="svc"><span class="svc__icon"><svg><use href="#i-shield"/></svg></span><div><h3>Safes</h3><p>Lorem Ipsum is simply dummy text of the printing and typesetting industry. Lorem Ipsum has been the industry's.</p></div></div>
      <div class="svc"><span class="svc__icon"><svg><use href="#i-question"/></svg></span><div><h3>Unsure What You Need?</h3><p>Lorem Ipsum is simply dummy text of the printing and typesetting industry. Lorem Ipsum has been the industry's.</p></div></div>
    </div>
    <div class="emergency">
      <div class="badge247">24/7</div>
      <div class="emergency__text"><b>EMERGENCY</b><strong>SERVICES</strong></div>
    </div>
    <div class="tollfree"><span class="tollfree__label">TOLL FREE NO</span><span class="tollfree__num">0800-417-2293</span></div>
    <div class="web web--light">www.harborlinelocks.com</div>
  </div>

  <article class="panel help">
    <svg class="help__art" viewBox="0 0 380 270">
      <path d="M0 0H380V140C372 210 250 230 190 265C130 230 8 210 0 140Z" fill="var(--black)"/>
      <path d="M0 150C10 215 130 225 190 262C250 225 370 215 380 150" fill="none" stroke="var(--gold)" stroke-width="7"/>
      <rect x="30" y="20" width="320" height="220" fill="#ecebe8" role="img" aria-label="Photo of a locksmith in blue overalls kneeling to fit a lock on an open door"/>
      <rect x="90" y="240" width="200" height="8" fill="var(--black)"/>
      <path d="M172 248h36l-18 16z" fill="var(--gold)"/>
    </svg>
    <div class="help__body">
      <h2>A LOCKSMITH <span class="gold">CAN HELP YOU WITH</span></h2>
      <h4>We have over 350 Vetted and Approved Locksmiths in the UK</h4>
      <p>Locksmiths approved by the National Locksmith Guild will be able to help if you're locked out of the house or flat, lost your key or need your door locks changing and replacing.</p>
      <p>Below are locksmiths services a locksmith can help you with:</p>
      <h5>1. Key Cutting</h5>
      <p>Whether you need a key cutting or have lost your keys and require a replacement key, a locksmith can help ranging from cutting normal house keys &amp; security keys to antique keys.</p>
      <h5>2. Door &amp; Window Locks</h5>
      <p>Whether you need a key cutting or have lost your keys and require a replacement key, a locksmith can help ranging from cutting normal house keys &amp; security keys to antique keys.</p>
      <div class="price"><div class="p1">LOCKSMITH SERVICES</div><div class="p2">STARTING AT <span class="gold">$39</span></div></div>
    </div>
    <div class="web">www.harborlinelocks.com</div>
  </article>
</section>

</body>
</html>
```